New Stationery New Logo for KT Fabrication Limited

We have a new logo and now want new stationary to go with it

This will be

Letterhead
Compliments Slip
Business Cards

Company details are
KT Fabrication Limited
Dellmoor Road, Rugby, Warwickshire, CV34 7HX, UK
Telephone : +44(0)1788 390617
Fax: +44(0)1788 473928
Email: sales@ktfabrication.co.uk
Web: www.ktfabrication.co.uk

Target Market(s)

Engineering / Metal Stamping

Industry/Entity Type

Manufacture

Contact Information for Business Card

Colin Brearley
Business Development Manager
KT Fabrication Limited
Dellmoor Road
Rugby
Warwickshire
CV34 7HX, UK

T: +44(0)1788 390617
F: +44(0)1788 473928
E: sales@ktfabrication.co.uk
W: www.ktfabrication.co.uk

Font styles to use
Sans Serif

Colors
33a6d7
0555a3
3176b5
85cae6
85acd3

Requirements
Must have
• Logo

```html
<!DOCTYPE html>
<html lang="en">
<head>
<meta charset="utf-8">
<title>KT Fabrication Limited — Stationery</title>
<link href="https://fonts.googleapis.com/css2?family=Open+Sans:wght@400;600&display=swap" rel="stylesheet">
<style>
  :root{
    --navy:#0555a3;
    --mid:#3176b5;
    --sky:#33a6d7;
    --pale:#85cae6;
    --soft:#85acd3;
    --ink:#1d1d1f;
    --paper:#ffffff;
    --slip-bg:#f4f4f5;
    --stage:#e9eaec;
  }
  *{box-sizing:border-box;margin:0;padding:0}
  html,body{width:1200px;height:867px;overflow:hidden}
  body{background:var(--stage);font-family:"Open Sans",Arial,sans-serif;color:var(--ink);position:relative}

  .sheet{position:absolute;background:var(--paper);box-shadow:0 2px 8px rgba(0,0,0,.15)}

  /* wordmark: one colour, one weight, one plain circle */
  .wordmark{display:flex;align-items:center;gap:8px;font-weight:600;letter-spacing:.28em;color:var(--ink);white-space:nowrap}
  .wordmark .dot{width:10px;height:10px;border-radius:50%;background:var(--navy);flex:none}
  .wordmark.light{color:#fff}
  .wordmark.light .dot{background:#fff}

  /* compliments slip */
  .slip{left:40px;top:40px;width:570px;height:270px;background:var(--slip-bg)}
  .slip .brand{position:absolute;left:22px;top:62px;font-size:14px}
  .slip .divider{position:absolute;left:212px;top:10px;width:1px;height:100px;background:var(--soft)}
  .slip .details{position:absolute;left:222px;top:12px;font-size:8.5px;line-height:1.45}
  .slip .details .co{color:var(--navy);font-size:9.5px}
  .slip .details .label{color:var(--navy)}
  .slip .details .gap{height:8px}
  .slip .side-tint{position:absolute;right:0;top:0;width:130px;height:232px;background:linear-gradient(180deg,#f4f4f5,#e6ecf4)}
  .slip .web{position:absolute;left:24px;bottom:46px;font-size:9px;color:var(--navy)}
  .slip .band{position:absolute;left:0;bottom:0;width:100%;height:38px;background:var(--navy);color:#fff;font-size:19px;text-align:right;padding:6px 24px 0 0}

  /* letterhead */
  .letterhead{left:660px;top:36px;width:500px;height:707px}
  .letterhead .brand{position:absolute;right:30px;top:34px;font-size:17px}
  .letterhead .band{position:absolute;left:0;top:82px;width:100%;height:24px;background:var(--navy);color:#fff;font-size:8px;display:flex;justify-content:space-between;align-items:center;padding:0 30px}
  .letterhead .footer{position:absolute;left:40px;right:40px;bottom:42px}
  .letterhead .footer .rule{height:1px;background:var(--mid)}
  .letterhead .footer .co{margin-top:10px;font-size:11px;color:var(--navy);font-weight:600}
  .letterhead .footer .addr{font-size:10px;font-weight:600}
  .letterhead .footer .web{font-size:10px;color:var(--navy);font-weight:600}

  /* business card front */
  .card{width:300px;height:190px}
  .card-front{left:40px;top:370px;background:linear-gradient(135deg,var(--mid),var(--navy) 55%,#0b3f86);overflow:hidden}
  .card-front .brand{position:absolute;left:50%;top:78px;transform:translateX(-50%);font-size:16px}
  .card-front .web{position:absolute;left:0;right:0;bottom:22px;text-align:center;font-size:8px;color:#d6e6f6}
  .card-front .lines{position:absolute;left:0;top:0;width:100%;height:100%}

  /* business card back */
  .card-back{left:360px;top:370px}
  .card-back .brand{position:absolute;right:18px;top:22px;font-size:13px}
  .card-back .person{position:absolute;left:20px;top:92px;display:flex;gap:8px;align-items:flex-start}
  .card-back .person .badge{width:16px;height:16px;background:var(--navy);flex:none}
  .card-back .person .name{font-size:10px;color:var(--navy);font-weight:600;letter-spacing:.04em}
  .card-back .person .role{font-size:7.5px}
  .card-back .divider{position:absolute;left:142px;top:88px;width:1px;height:76px;background:var(--soft)}
  .card-back .contacts{position:absolute;left:152px;top:90px;list-style:none;font-size:7.5px;line-height:1.75}
  .card-back .contacts li{display:flex;align-items:center;gap:5px}
  .card-back .contacts svg{flex:none}
</style>
</head>
<body>

<section class="sheet slip" aria-label="Compliments slip">
  <div class="side-tint"></div>
  <div class="wordmark brand"><span>KT FABRICATION</span><span class="dot"></span></div>
  <div class="divider"></div>
  <div class="details">
    <div class="co">KT Fabrication Limited</div>
    <div>Dellmoor Road,</div>
    <div>Rugby, Warwickshire,</div>
    <div>CV34 7HX, UK</div>
    <div class="gap"></div>
    <div><span class="label">Email - sales@ktfabrication.co.uk</span></div>
    <div><span class="label">Tel. -</span> +44(0)1788 390617</div>
    <div><span class="label">Fax.-</span> +44(0)1788 473928</div>
  </div>
  <div class="web">www.ktfabrication.co.uk</div>
  <div class="band">With Compliments...</div>
</section>

<section class="sheet letterhead" aria-label="Letterhead">
  <div class="wordmark brand"><span>KT FABRICATION</span><span class="dot"></span></div>
  <div class="band">
    <span>Email - sales@ktfabrication.co.uk</span>
    <span>Tel. - +44(0)1788 390617</span>
    <span>Fax. - +44(0)1788 473928</span>
  </div>
  <div class="footer">
    <div class="rule"></div>
    <div class="co">KT Fabrication Limited</div>
    <div class="addr">Dellmoor Road, Rugby, Warwickshire, CV34 7HX, UK</div>
    <div class="web">www.ktfabrication.co.uk</div>
  </div>
</section>

<section class="sheet card card-front" aria-label="Business card front">
  <svg class="lines" viewBox="0 0 300 190" aria-hidden="true">
    <g stroke="#ffffff" stroke-opacity=".08" stroke-width="1">
      <line x1="20" y1="0" x2="20" y2="80"/><line x1="28" y1="0" x2="28" y2="80"/>
      <line x1="36" y1="0" x2="36" y2="80"/><line x1="44" y1="0" x2="44" y2="80"/>
      <line x1="0" y1="178" x2="300" y2="178"/>
    </g>
  </svg>
  <div class="wordmark light brand"><span>KT FABRICATION</span><span class="dot"></span></div>
  <div class="web">www.ktfabrication.co.uk</div>
</section>

<section class="sheet card card-back" aria-label="Business card back">
  <div class="wordmark brand"><span>KT FABRICATION</span><span class="dot"></span></div>
  <div class="person">
    <span class="badge"></span>
    <div>
      <div class="name">YOUR NAME</div>
      <div class="role">Position</div>
    </div>
  </div>
  <div class="divider"></div>
  <ul class="contacts">
    <li><svg width="8" height="8" viewBox="0 0 8 8"><rect width="8" height="8" rx="1.5" fill="#0555a3"/></svg>+44(0)1788 390617</li>
    <li><svg width="8" height="8" viewBox="0 0 8 8"><rect width="8" height="8" rx="1.5" fill="#0555a3"/></svg>+44(0)1788 473928</li>
    <li><svg width="8" height="8" viewBox="0 0 8 8"><rect width="8" height="8" rx="1.5" fill="#0555a3"/></svg>sales@ktfabrication.co.uk</li>
    <li><svg width="8" height="8" viewBox="0 0 8 8"><rect width="8" height="8" rx="1.5" fill="#0555a3"/></svg>www.ktfabrication.co.uk</li>
  </ul>
</section>

</body>
</html>
```